BOLD & MINIMALIST DESIGN NEEDED

We want a very bold but minimalistic business card design that is impactful and utilizes both sides of the business card. Our current logo is included for your use.

We want bold fonts and good use of negative space. We don't want the logo to overpower the design.

Target Market(s)

Professionals who are building new commercial buildings.

Industry/Entity Type

Construction

Contact Information for Business Card

Name, Title, email, office phone, cell phone, website

Font styles to use
Serif
Sans Serif

Requirements
Must have
• Bold design!

```html
<!DOCTYPE html>
<html lang="en">
<head>
<meta charset="utf-8">
<title>Ridgeline Design + Build — Business Card</title>
<link rel="stylesheet" href="https://fonts.googleapis.com/css2?family=Poppins:wght@400;500;600;800&display=swap">
<style>
  :root {
    --stage: #2b2b2b;
    --ink: #111111;
    --card-dark: #1c1c1c;
    --paper: #ffffff;
    --accent: #7cc242;
    --text: #1a1a1a;
  }
  * { margin: 0; padding: 0; box-sizing: border-box; }
  html, body { width: 1200px; height: 875px; overflow: hidden; }
  body {
    background: var(--stage);
    font-family: "Poppins", sans-serif;
    display: flex;
    align-items: center;
    justify-content: center;
    gap: 40px;
  }
  .card {
    position: relative;
    width: 540px;
    height: 309px;
    border-radius: 14px;
    overflow: hidden;
    box-shadow: 0 18px 40px rgba(0,0,0,.45);
  }
  .card--back {
    background: var(--card-dark);
    display: flex;
    align-items: center;
    justify-content: center;
  }
  .wordmark {
    display: flex;
    align-items: center;
    gap: 12px;
    font-weight: 800;
    letter-spacing: 1px;
    line-height: 1;
  }
  .wordmark__square {
    width: 26px;
    height: 26px;
    background: var(--accent);
  }
  .card--back .wordmark { font-size: 44px; color: var(--paper); }
  .card--front { background: var(--paper); border-radius: 6px; }
  .card--front .wordmark {
    position: absolute;
    left: 34px;
    top: 112px;
    font-size: 30px;
    color: var(--ink);
  }
  .card--front .wordmark__square { width: 18px; height: 18px; }
  .divider {
    position: absolute;
    left: 290px;
    top: 50px;
    width: 1.5px;
    height: 150px;
    background: var(--accent);
  }
  .contact {
    position: absolute;
    left: 312px;
    top: 44px;
    color: var(--text);
  }
  .contact__name {
    font-size: 20px;
    font-weight: 600;
    color: var(--accent);
    line-height: 1.1;
  }
  .contact__title { font-size: 11px; margin-bottom: 10px; }
  .contact__list { list-style: none; font-size: 11px; line-height: 1.6; }
  .contact__list li { display: flex; align-items: center; gap: 7px; }
  .contact__list svg { width: 10px; height: 10px; fill: var(--accent); flex: none; }
  .contact__address { margin-top: 8px; font-size: 11px; font-weight: 500; line-height: 1.45; }
  .swoosh { position: absolute; left: 0; bottom: 0; width: 540px; height: 120px; }
</style>
</head>
<body>

  <section class="card card--back" aria-label="Card back">
    <div class="wordmark"><span class="wordmark__square"></span>RIDGELINE</div>
  </section>

  <section class="card card--front" aria-label="Card front">
    <div class="wordmark"><span class="wordmark__square"></span>RIDGELINE</div>
    <div class="divider"></div>
    <div class="contact">
      <p class="contact__name">Daniel Carter</p>
      <p class="contact__title">Head contractor</p>
      <ul class="contact__list">
        <li><svg viewBox="0 0 10 10"><path d="M2 1l2 2-1 1.2a6 6 0 0 0 2.8 2.8L7 6l2 2-1.3 1.3C4.5 9 1 5.5.7 2.3z"/></svg>555.310.4400</li>
        <li><svg viewBox="0 0 10 10"><path d="M3 0h4a1 1 0 0 1 1 1v8a1 1 0 0 1-1 1H3a1 1 0 0 1-1-1V1a1 1 0 0 1 1-1zm0 1.5v6h4v-6z"/></svg>555-310-4401</li>
        <li><svg viewBox="0 0 10 10"><path d="M0 2h10v6H0zm1 1v.3l4 2.4 4-2.4V3z"/></svg>info@rdb-build.com</li>
        <li><svg viewBox="0 0 10 10"><circle cx="5" cy="5" r="4.5"/></svg>www.rdb-build.com</li>
      </ul>
      <p class="contact__address">1420 Cedar Ridge Rd.<br>Pine Hollow, GA 30512</p>
    </div>
    <svg class="swoosh" viewBox="0 0 540 120" preserveAspectRatio="none" aria-hidden="true">
      <path d="M0 120 C120 40 330 30 540 0 L540 120 Z" fill="#111111"/>
    </svg>
  </section>

</body>
</html>
```